Bold Website Redesign for a Disruptive Training Brand

Brightmoor Labs is a bold, no-fluff sales & leadership training company powered by AI-driven practice and behavioral science. We’ve already built our website structure and copy in Craftly.io — now we need a designer to fully transform the visual design across all pages (Home, Approach, Programs, About, Contact).
We’re looking for a modern, memorable, high-performance aesthetic that blends human energy, science, and tech without feeling corporate or safe. Clean, bold typography, fluid layout, strong emotional hero moments, subtle motion, and imagery that mixes real people with abstract scientific/tech visuals.Because our clients are primarily North American, please ensure any human photography or AI-generated imagery reflects a North American business context and demographics (modern, diverse, and realistic).

Your job is visual redesign only — no coding required.
The final design must be practical to rebuild inside Craftly.io.

A full, detailed creative brief (plus logo files) is included in the uploaded files.
If you can bring a mix of edge, intelligence, and strong visual storytelling, we’d love to see your work.

Website is already built in Craftly.io at - https://brightmoor-website-tempdesign.craftly.app — structure is set, visuals need redesign.

```html
<!DOCTYPE html>
<html lang="en">
<head>
<meta charset="utf-8">
<title>Brightmoor Labs — Training That Practices Back</title>
<link rel="stylesheet" href="https://fonts.googleapis.com/css2?family=Montserrat:wght@400;500;600;700;800&display=swap">
<style>
:root{
  --navy:#0b1f45;
  --blue:#3a63b0;
  --blue-title:#2d5eb3;
  --cyan:#39b3e5;
  --ink:#111a2e;
  --text:#5a6172;
  --white:#ffffff;
}
*{box-sizing:border-box;margin:0;padding:0}
html,body{width:1200px;height:4178px;overflow:hidden}
body{position:relative;background:var(--white);font-family:"Montserrat",sans-serif;color:var(--ink)}
.abs{position:absolute}
.brand{font-family:"Montserrat",sans-serif;font-weight:800;color:var(--navy);font-size:14px;letter-spacing:2px;white-space:nowrap;display:flex;align-items:center;justify-content:center}
.nav-links{display:flex;gap:28px;font-size:11px;color:#333}
.btn{display:inline-flex;align-items:center;justify-content:center;gap:10px;background:var(--blue);color:var(--white);font-size:10.5px;font-weight:700;letter-spacing:.5px;text-transform:uppercase;border-radius:3px}
.btn svg{width:18px;height:8px}
.btn-light{background:var(--white);color:var(--navy)}
h1,h2,h3{font-weight:700;text-transform:uppercase}
.center{text-align:center}
.link{font-size:11px;text-decoration:underline;letter-spacing:.4px;text-transform:uppercase}

/* hero */
.hero{left:0;top:0;width:1200px;height:843px;background:
  radial-gradient(ellipse 460px 400px at 600px 800px,rgba(143,177,221,.75) 0%,rgba(201,220,239,.6) 45%,rgba(255,255,255,0) 100%),
  linear-gradient(180deg,#ffffff 0%,#f3f6fb 45%,#dde5f2 100%)}
.hero-title{left:0;top:180px;width:1200px;font-size:55px;line-height:62px;color:var(--navy);letter-spacing:1px}
.hero-title span{color:var(--blue-title)}
.hero-sub{left:0;top:314px;width:1200px;font-size:14px;color:#3c4353}
.hero-body{left:270px;top:342px;width:660px;font-size:12.5px;line-height:19px;color:#3c4353}

/* practice card */
.practice{left:112px;top:606px;width:975px;height:403px;border-radius:8px;background:linear-gradient(160deg,#1a3a78 0%,#0d2452 55%,#0a1d43 100%);color:var(--white)}
.practice h2{position:absolute;left:70px;top:62px;font-size:31px;line-height:41px;letter-spacing:1px}
.practice .lede{position:absolute;left:561px;top:88px;width:320px;font-size:11.5px;line-height:16px;color:#dfe6f3}
.pillar{position:absolute;top:200px;width:260px}
.pillar .icon{width:46px;height:46px}
.pillar h3{margin-top:28px;font-size:14px;letter-spacing:.6px}
.pillar p{margin-top:12px;font-size:11.5px;line-height:14px;color:#e3e9f5}

/* drives */
.drives-title{left:0;top:1078px;width:1200px;font-size:31px;letter-spacing:1px}
.drives-body{left:270px;top:1124px;width:660px;font-size:11.5px;line-height:17px;color:var(--text)}

.card{border-radius:8px;overflow:hidden}
.belief{left:112px;top:1281px;width:481px;height:272px;background:var(--white);box-shadow:0 2px 10px rgba(15,35,80,.08)}
.belief-glow{position:absolute;left:270px;top:-30px;width:240px;height:240px;background:radial-gradient(circle,rgba(58,99,176,.55) 0%,rgba(169,200,234,.5) 40%,rgba(238,243,250,.6) 70%,rgba(255,255,255,0) 100%)}
.belief h3,.effort h3{position:absolute;top:84px;font-size:19px;letter-spacing:.6px}
.belief p,.effort p{position:absolute;top:116px;font-size:11.5px;line-height:16px}
.effort{left:607px;top:1281px;width:480px;height:272px;background:radial-gradient(circle at 70% 30%,#1f5a7e 0%,#113a60 35%,#0b2447 70%,#09203f 100%);color:var(--white)}

.problem{left:112px;top:1565px;width:975px;height:293px;background:var(--white);box-shadow:0 2px 10px rgba(15,35,80,.08)}
.problem h3{position:absolute;left:55px;top:80px;width:440px;font-size:19px;line-height:25px;letter-spacing:.5px}
.problem p{position:absolute;left:55px;top:137px;width:420px;font-size:11.5px;line-height:16px;color:var(--text)}

/* team */
.team{left:0;top:1934px;width:1200px;height:576px;background:var(--navy);color:var(--white)}
.team h2{position:absolute;left:112px;top:70px;font-size:32px;line-height:41px;letter-spacing:1px}
.team .lede{position:absolute;left:673px;top:78px;width:415px;font-size:11.5px;line-height:16px;color:#dbe3f2}
.member{position:absolute;top:257px;width:317px;height:225px;border-radius:8px;background:rgba(38,62,110,.55)}
.member .photo{position:absolute;right:30px;top:26px;width:62px;height:62px;border-radius:50%;background:radial-gradient(circle,#8a6a55 0%,#5a4a48 60%,#304f88 100%)}
.member h3{position:absolute;left:32px;top:50px;font-size:14px;letter-spacing:.4px}
.member .role{position:absolute;left:32px;top:72px;font-size:11px;line-height:15px;color:var(--cyan)}
.member p{position:absolute;left:32px;width:265px;font-size:11px;line-height:16px;color:#e3e9f5}

/* make it happen */
.happen-title{left:0;top:2568px;width:1200px;font-size:31px;letter-spacing:1px}
.happen-body{left:330px;top:2616px;width:540px;font-size:11.5px;line-height:17px;color:var(--text)}
.cta-card{top:2710px;width:480px;height:228px;color:var(--white)}
.cta-card h3{position:absolute;left:55px;top:62px;font-size:19px;letter-spacing:.6px}
.cta-card p{position:absolute;left:55px;top:96px;width:340px;font-size:11.5px;line-height:16px}
.touch{left:112px;background:linear-gradient(160deg,#173772,#0b2149)}
.mastery{left:607px;background:linear-gradient(120deg,#3fb6e4 0%,#2c89c2 45%,#163f78 80%,#0e2a57 100%)}
.mastery h3,.mastery p{left:43px}

/* reviews */
.review-glow{left:0;top:2940px;width:600px;height:630px;background:radial-gradient(circle at 276px 320px,rgba(106,179,230,.8) 0%,rgba(182,209,236,.7) 35%,rgba(219,232,244,.6) 65%,rgba(241,245,250,.5) 85%,rgba(255,255,255,0) 100%)}
.review-title{left:590px;top:3160px;width:500px;font-size:34px;line-height:38px;color:var(--navy);letter-spacing:.5px}
.review-text{left:590px;width:480px;font-size:10px;line-height:13px;color:#6b7180}
.dot{top:3480px;width:11px;height:11px;border-radius:50%;background:#d5d9e2}

/* closing */
.footer-band{left:0;top:3697px;width:1200px;height:481px;background:#f1f3f8}
.closing{left:112px;top:3569px;width:975px;height:268px;border-radius:8px;background:linear-gradient(160deg,#173772,#0b2149)}
.closing h2{position:absolute;left:0;top:62px;width:975px;font-size:34px;line-height:42px;color:var(--white);letter-spacing:1px;text-align:center}
.closing h2 span{color:var(--cyan)}
.footer-links{left:0;top:3961px;width:1200px;justify-content:center;gap:30px}
.contact{top:4002px;display:flex;align-items:center;gap:8px;font-size:10.5px;color:#333}
.contact svg{width:14px;height:14px}
.social{top:4053px;width:24px;height:24px;border-radius:50%;background:var(--blue)}
</style>
</head>
<body>

<section class="abs hero" aria-label="Hero"></section>

<header>
  <nav class="abs nav-links" style="left:112px;top:38px">
    <span>Approach</span><span>Programs</span><span>About</span><span>Contact</span>
  </nav>
  <div class="abs brand" style="left:500px;top:36px;width:200px">BRIGHTMOOR LABS</div>
  <svg class="abs" style="left:928px;top:36px" width="16" height="16" viewBox="0 0 16 16" aria-label="Search"><circle cx="7" cy="7" r="5" fill="none" stroke="#333" stroke-width="1.3"/><path d="M11 11l4 4" stroke="#333" stroke-width="1.3"/></svg>
  <span class="abs btn" style="left:968px;top:26px;width:119px;height:36px">Let's Talk</span>
</header>

<h1 class="abs hero-title center"><span>Training</span> That<br>Practices Back.</h1>
<p class="abs hero-sub center">AI-driven sustainment that builds mastery — so you don't have to.</p>
<p class="abs hero-body center">You'll see measurable growth as your people turn insight into habit — automatically, sustainably,<br>and without extra work for their leaders.</p>
<span class="abs btn" style="left:512px;top:399px;width:174px;height:36px">See How We Do It <svg viewBox="0 0 18 8"><path d="M0 4h16M13 1l3 3-3 3" fill="none" stroke="#fff" stroke-width="1.2"/></svg></span>

<section class="abs practice">
  <h2>Practice Made<br>Permanent.</h2>
  <p class="lede">You'll replace "hope they remember" with a system that makes sure they do.</p>
  <div class="pillar" style="left:71px">
    <svg class="icon" viewBox="0 0 46 46" aria-hidden="true"><circle cx="23" cy="23" r="21" fill="#3ab4e6"/><path d="M23 8v30M13 16h6v6M33 16h-6v6M13 30h6v-5M33 30h-6v-5" fill="none" stroke="#0d2452" stroke-width="2.2" stroke-linecap="round"/></svg>
    <h3>Learn</h3>
    <p>Fast, focused workshops, built on science, that install the mindset and skills that matter most.</p>
  </div>
  <div class="pillar" style="left:389px">
    <svg class="icon" viewBox="0 0 46 46" aria-hidden="true"><path d="M23 2l5 4 6-1 2 6 6 3-2 6 2 6-6 3-2 6-6-1-5 4-5-4-6 1-2-6-6-3 2-6-2-6 6-3 2-6 6 1z" fill="#3ab4e6"/><circle cx="23" cy="23" r="11" fill="none" stroke="#0d2452" stroke-width="2.2"/><path d="M18 23l4 4 6-7" fill="none" stroke="#0d2452" stroke-width="2.4" stroke-linecap="round"/></svg>
    <h3>Certify</h3>
    <p>Programmatic AI-driven practice and feedback - mastery without management overhead.</p>
  </div>
  <div class="pillar" style="left:708px">
    <svg class="icon" viewBox="0 0 46 46" aria-hidden="true"><rect x="2" y="26" width="11" height="18" fill="#3ab4e6"/><rect x="17" y="6" width="11" height="38" fill="#3ab4e6"/><rect x="32" y="18" width="11" height="26" fill="#3ab4e6"/></svg>
    <h3>Sustain</h3>
    <p>Light-touch challenges and dashboards that keep skills sharp long after training ends.</p>
  </div>
</section>

<h2 class="abs drives-title center">What Drives Us</h2>
<p class="abs drives-body center">We believe leadership and sales excellence are skills that can be practiced, measured, and sustained. Our work makes that practice automatic — so growth depends on design, not intention.</p>
<span class="abs btn" style="left:506px;top:1177px;width:188px;height:36px">Start a Conversation <svg viewBox="0 0 18 8"><path d="M0 4h16M13 1l3 3-3 3" fill="none" stroke="#fff" stroke-width="1.2"/></svg></span>

<article class="abs card belief">
  <div class="belief-glow" role="img" aria-label="Soft blue glow decoration"></div>
  <h3 style="left:55px">Our Belief</h3>
  <p style="left:55px;width:190px;color:var(--text)">Making learning that sticks through AI-driven sustainment and behavioral science.</p>
  <span class="abs link" style="left:55px;top:176px;color:var(--blue)">More About Us</span>
</article>

<article class="abs card effort" role="img" aria-label="Abstract network of glowing neurons on deep blue">
  <h3 style="left:43px">Less Effort. More Mastery.</h3>
  <p style="left:43px;width:370px;color:#e3e9f5">Because we've designed sustainment into the system, your leaders don't have to force it. Your people practice. The platform measures. You get lasting capability — automatically.</p>
  <span class="abs link" style="left:43px;top:176px;color:var(--white)">See Our Programs</span>
</article>

<article class="abs card problem">
  <h3>The Real Problem Isn't Your People — It's The Forgetting Curve.</h3>
  <p>Within a week, most training disappears. Leaders are left guessing who's using what they learned — and no one has time to fix it. We built Brightmoor Labs to make progress automatic, measurable, and real.</p>
  <span class="abs link" style="left:55px;top:203px;color:var(--blue)">Watch How Sustained Practice Changes The Curve</span>
  <svg class="abs" style="left:537px;top:37px" width="438" height="227" viewBox="0 0 438 227" aria-label="Line chart of knowledge retention dropping over a week">
    <rect width="438" height="227" fill="#f7f8fa"/>
    <defs><linearGradient id="fade" x1="0" y1="0" x2="0" y2="1"><stop offset="0" stop-color="#f4b4bc"/><stop offset="1" stop-color="#fde3e6"/></linearGradient></defs>
    <path d="M16 68 C80 80 150 120 210 150 S330 180 438 173 V213 H16 Z" fill="url(#fade)"/>
    <path d="M16 68 C80 80 150 120 210 150 S330 180 438 173" fill="none" stroke="#e98a96" stroke-width="1.4"/>
    <path d="M16 78 L80 80 L210 86 L340 92 L438 90" fill="none" stroke="#8ea8d8" stroke-width="2"/>
    <circle cx="80" cy="80" r="4" fill="#8ea8d8"/><circle cx="210" cy="86" r="4" fill="#8ea8d8"/><circle cx="340" cy="92" r="4" fill="#8ea8d8"/>
    <text x="28" y="52" font-family="Montserrat,sans-serif" font-size="11" fill="#5a6172">People forget fast.</text>
    <text x="232" y="104" font-family="Montserrat,sans-serif" font-size="11" fill="#5a6172">Within a week, 70% is gone.</text>
  </svg>
</article>

<section class="abs team">
  <h2>Built By People<br>Who've Led The<br>Change Themselves.</h2>
  <p class="lede">Behind Brightmoor Labs are leaders who've lived the challenge of making learning last. They've scaled companies, built cultures, and led transformation — and now they've designed the system they always wished existed.</p>
  <span class="abs btn" style="left:673px;top:156px;width:143px;height:36px">Meet The Team <svg viewBox="0 0 18 8"><path d="M0 4h16M13 1l3 3-3 3" fill="none" stroke="#fff" stroke-width="1.2"/></svg></span>

  <div class="member" style="left:112px">
    <div class="photo" role="img" aria-label="Portrait of Dan Holloway"></div>
    <h3>Dan Holloway</h3>
    <span class="role">Co-Founder &amp; CEO</span>
    <p style="top:96px">Growth strategist and technologist, expert in scaling teams through insight and analytics. Dan brings deep experience in translating data into actionable capability development.</p>
  </div>
  <div class="member" style="left:443px">
    <div class="photo" role="img" aria-label="Portrait of Mark Denton"></div>
    <h3>Mark Denton</h3>
    <span class="role">Co-Founder &amp; Chief<br>Strategy Officer</span>
    <p style="top:114px">Veteran leader in organizational alignment and culture transformation. Mark has helped hundreds of companies build cohesive, high-performing teams at scale.</p>
  </div>
  <div class="member" style="left:770px">
    <div class="photo" role="img" aria-label="Portrait of Paul Whitaker"></div>
    <h3>Paul Whitaker</h3>
    <span class="role">Co-Founder &amp; Chief<br>Growth Officer</span>
    <p style="top:114px">Expert in human capital and science-based training design, focused on measurable performance outcomes. Paul ensures our programs deliver real, lasting results.</p>
  </div>
</section>

<h2 class="abs happen-title center">Make It Happen</h2>
<p class="abs happen-body center">Lasting growth starts with one — a real conversation about what's working, what's not, and what's possible.</p>

<article class="abs card cta-card touch">
  <h3>Get In Touch</h3>
  <p>Whether you're exploring training or curious about our model, we'll help you find the right path — no pressure, no script.</p>
  <span class="abs link" style="left:55px;top:157px;color:var(--cyan)">Send Message</span>
</article>
<article class="abs card cta-card mastery">
  <h3>Leadership Mastery</h3>
  <p style="width:380px"><strong style="font-size:10.5px;color:#123a72">Build leaders who create lasting impact</strong><br>Develop leaders who create clarity, coach for growth, and drive results that last — even amid real-world complexity.</p>
  <span class="abs link" style="left:43px;top:157px;color:#123a72">Talk With Us About Leadership Mastery</span>
</article>

<div class="abs review-glow" role="img" aria-label="Soft blue glow behind client photo"></div>
<div class="abs" style="left:162px;top:3073px;width:262px;height:496px;border-radius:120px 120px 0 0;background:linear-gradient(180deg,#c8a890 0%,#9b7e6c 35%,#6e5c54 100%)" role="img" aria-label="Photo of a smiling client in a checked blazer giving two thumbs up"></div>
<h2 class="abs review-title">Great Reviews From<br>Our Clients</h2>
<p class="abs review-text" style="top:3254px">Working with the team reshaped how our managers coach every week. The practice prompts feel natural, and the results showed up in our numbers within a single quarter.</p>
<p class="abs review-text" style="top:3308px">Our leaders now practice without reminders, and the habits have stuck long after the workshops ended.</p>
<p class="abs" style="left:590px;top:3364px;font-size:11px;font-weight:700;color:#333">ELLEN R.</p>
<span class="abs dot" style="left:1032px;background:var(--cyan)"></span>
<span class="abs dot" style="left:1054px"></span>
<span class="abs dot" style="left:1076px"></span>

<div class="abs footer-band"></div>
<section class="abs closing">
  <h2><span>Ready To See</span> What Lasting<br>Capability Looks Like?</h2>
  <span class="abs btn" style="left:297px;top:161px;width:219px;height:37px">Start a Conversation <svg viewBox="0 0 18 8"><path d="M0 4h16M13 1l3 3-3 3" fill="none" stroke="#fff" stroke-width="1.2"/></svg></span>
  <span class="abs btn btn-light" style="left:530px;top:161px;width:148px;height:37px">Learn More <svg viewBox="0 0 18 8"><path d="M0 4h16M13 1l3 3-3 3" fill="none" stroke="#0b1f45" stroke-width="1.2"/></svg></span>
</section>

<footer>
  <div class="abs brand" style="left:500px;top:3890px;width:200px">BRIGHTMOOR LABS</div>
  <nav class="abs nav-links footer-links"><span>Approach</span><span>Programs</span><span>About</span><span>Contact</span></nav>
  <div class="abs contact" style="left:258px">
    <svg viewBox="0 0 14 14" aria-hidden="true"><path d="M7 1a4.5 4.5 0 0 0-4.5 4.5C2.5 9 7 13 7 13s4.5-4 4.5-7.5A4.5 4.5 0 0 0 7 1z" fill="#111"/><circle cx="7" cy="5.5" r="1.6" fill="#f1f3f8"/></svg>
    4820 W Canyon Ridge Rd Suite 210, Tempe, AZ 85282
  </div>
  <div class="abs contact" style="left:584px">
    <svg viewBox="0 0 14 14" aria-hidden="true"><rect x="1" y="3" width="12" height="9" fill="#111"/><path d="M1 3l6 5 6-5" fill="none" stroke="#f1f3f8" stroke-width="1"/></svg>
    contact@brightmoorlabs.com
  </div>
  <div class="abs contact" style="left:828px">
    <svg viewBox="0 0 14 14" aria-hidden="true"><path d="M3 1l3 3-1.5 2a8 8 0 0 0 3.5 3.5L10 8l3 3-2 2C6 13 1 8 1 3z" fill="#111"/></svg>
    +1 (480) 555-0142
  </div>
  <div class="abs" style="left:112px;top:4064px;width:398px;height:1px;background:#9aa6c2"></div>
  <div class="abs" style="left:690px;top:4064px;width:397px;height:1px;background:#9aa6c2"></div>
  <span class="abs social" style="left:525px" aria-label="Social profile"></span>
  <span class="abs social" style="left:565px" aria-label="Social profile"></span>
  <span class="abs social" style="left:605px" aria-label="Social profile"></span>
  <span class="abs social" style="left:645px" aria-label="Social profile"></span>
  <p class="abs center" style="left:0;top:4118px;width:1200px;font-size:10px;color:#555">© 2025 Brightmoor Labs. All rights reserved.</p>
</footer>

</body>
</html>
```